Business Card Design

We need a business card for a new business based in Sydney, Australia. It is a home based baking business, the key products are cookies and muffins and slices including gluten free baked goods. With the emphasis on home made baking. The target market is cafes, coffee shops and vans, restaurants. Products may be provided in display jars or individually wrapped. The final design should be in the colours pink, purple.

Industry/Entity Type

Business

Contact Information for Business Card

Pindle's Bakery Pty Ltd, Maren Tulloch, maren@pindlesbakery.com.au
0412 506 218, www.pindlesbakery.com.au, ACN 581 246 037,

```html
<!DOCTYPE html>
<html lang="en">
<head>
<meta charset="utf-8">
<title>Pindle's Bakery – Business Card</title>
<link rel="stylesheet" href="https://fonts.googleapis.com/css2?family=Alfa+Slab+One&family=Exo+2:wght@400;500&display=swap">
<style>
  :root {
    --backdrop: #d9d6d2;
    --card-light: #ffffff;
    --card-shade: #e4e4e6;
    --pink: #e8406a;
    --pink-soft: #f0567c;
    --purple: #8a3a8e;
    --indigo: #3f3c9a;
    --ink: #3a3a3a;
  }
  html, body {
    margin: 0;
    width: 1200px;
    height: 677px;
    overflow: hidden;
    background: var(--backdrop);
  }
  .card {
    position: absolute;
    left: 75px;
    top: 38px;
    width: 1050px;
    height: 600px;
    overflow: hidden;
    background: radial-gradient(ellipse at 40% 45%, var(--card-light) 0%, #f4f4f5 45%, var(--card-shade) 100%);
    box-shadow: 0 18px 40px rgba(0,0,0,0.25);
  }
  .card__rings {
    position: absolute;
    inset: 0;
  }
  .brand {
    position: absolute;
    left: 150px;
    top: 150px;
    margin: 0;
    font-family: "Alfa Slab One", serif;
    font-weight: 400;
    font-size: 66px;
    letter-spacing: 1px;
    color: var(--pink);
  }
  .person {
    position: absolute;
    left: 250px;
    top: 268px;
    font-family: "Exo 2", sans-serif;
  }
  .person__name {
    margin: 0;
    font-size: 30px;
    font-weight: 500;
    letter-spacing: 2px;
    color: var(--indigo);
  }
  .person__role {
    margin: 4px 0 0;
    font-size: 22px;
    color: var(--ink);
  }
  .contact {
    position: absolute;
    right: 48px;
    top: 200px;
    margin: 0;
    padding: 0;
    list-style: none;
    font-family: "Exo 2", sans-serif;
    font-size: 19px;
    color: var(--ink);
    text-align: right;
  }
  .contact__item {
    display: flex;
    justify-content: flex-end;
    align-items: center;
    gap: 12px;
    margin-bottom: 14px;
  }
  .contact__item--address { align-items: flex-start; line-height: 1.35; }
  .contact__icon { width: 20px; height: 20px; flex: none; }
</style>
</head>
<body>
  <section class="card" aria-label="Pindle's Bakery business card">
    <svg class="card__rings" width="1050" height="600" viewBox="0 0 1050 600" aria-hidden="true">
      <circle cx="40" cy="610" r="150" fill="none" stroke="var(--purple)" stroke-width="48"/>
      <circle cx="470" cy="650" r="205" fill="none" stroke="var(--pink-soft)" stroke-width="50"/>
    </svg>

    <h1 class="brand">Pindle's Bakery</h1>

    <div class="person">
      <p class="person__name">EWAN DORRIGO</p>
      <p class="person__role">Managing Director</p>
    </div>

    <ul class="contact">
      <li class="contact__item contact__item--address">
        <span>041 12th Floor, Mall<br>Harbour Road NSW</span>
        <svg class="contact__icon" viewBox="0 0 20 20"><path d="M10 1a6 6 0 0 0-6 6c0 5 6 12 6 12s6-7 6-12a6 6 0 0 0-6-6z" fill="var(--pink)"/><circle cx="10" cy="7" r="2.2" fill="#fff"/></svg>
      </li>
      <li class="contact__item">
        <span>013 246 5790</span>
        <svg class="contact__icon" viewBox="0 0 20 20"><path d="M5 2l3 4-2 2c1 2.5 3.5 5 6 6l2-2 4 3-2 3c-7 0-14-7-14-14z" fill="var(--pink)"/></svg>
      </li>
      <li class="contact__item">
        <span>013 246 5790</span>
        <svg class="contact__icon" viewBox="0 0 20 20"><rect x="5" y="1" width="10" height="18" rx="2" fill="var(--pink)"/><rect x="7" y="3.5" width="6" height="10" fill="#fff"/></svg>
      </li>
      <li class="contact__item">
        <span>hello@pindlesmail.com</span>
        <svg class="contact__icon" viewBox="0 0 20 20"><rect x="1" y="4" width="18" height="12" rx="1.5" fill="var(--pink)"/><path d="M2 5l8 6 8-6" fill="none" stroke="#fff" stroke-width="1.5"/></svg>
      </li>
      <li class="contact__item">
        <span>www.pindlesbakery.com.au</span>
        <svg class="contact__icon" viewBox="0 0 20 20"><circle cx="10" cy="10" r="8.5" fill="none" stroke="var(--pink)" stroke-width="1.8"/><ellipse cx="10" cy="10" rx="3.5" ry="8.5" fill="none" stroke="var(--pink)" stroke-width="1.5"/><path d="M2 10h16" stroke="var(--pink)" stroke-width="1.5"/></svg>
      </li>
    </ul>
  </section>
</body>
</html>
```